Cosmetics Brand Logo and Bottle Label Design

We are creating a new cosmetics brand called "Nolan Whitby" and would like you to create an amazing logo and bottle label for this brand's new 100% pure argan oil product.
For the logo, we really like the logo's of Marin Calloway and Vessa. The text should be Sans Serif (without feet).
For the actual bottle label, please find attached labels of one of our competitors design which really like. We really like the simplicity and elegance of the design. The only difference is that our product will be using light turqoise as the brand color. Please feel free to add your own creativity into it as well.
Industry/Entity Type
Cosmetics
Logo Text
Nolan Whitby
Font styles to use

```html
<!DOCTYPE html>
<html lang="en">
<head>
<meta charset="utf-8">
<title>Nolan Whitby – Argan Oil Brand Board</title>
<link rel="stylesheet" href="https://fonts.googleapis.com/css2?family=Yanone+Kaffeesatz:wght@400;500&family=PT+Sans&family=Parisienne&display=swap">
<style>
  :root {
    --teal: #35b7a2;
    --teal-light: #84d0c6;
    --teal-pale: #c5eae3;
    --gold: #f3d57a;
    --cream: #fdf2d8;
    --brown: #6b2a0c;
    --brown-dark: #3d1505;
    --ink: #1c1c1c;
    --board: #f1e9e6;
    --paper: #f2f1f1;
    --text-body: #4a3a32;
  }
  * { box-sizing: border-box; margin: 0; padding: 0; }
  html, body { width: 1200px; height: 1086px; overflow: hidden; }
  body {
    position: relative;
    background: linear-gradient(180deg, #f8f2ee 0%, var(--board) 100%);
    font-family: "PT Sans", sans-serif;
  }
  .panel { position: absolute; left: 14px; width: 530px; overflow: hidden; }
  .panel--mono { top: 8px; height: 346px; background: linear-gradient(180deg, #e9e8e7 0%, #bdbbbb 100%); }
  .panel--color { top: 372px; height: 346px; background: linear-gradient(180deg, var(--teal-pale) 0%, var(--teal) 100%); }
  .panel--color .panel__card {
    position: absolute; left: 44px; top: 38px; width: 442px; height: 277px;
    background: linear-gradient(180deg, #eef0c4 0%, #e3bf7c 100%);
  }
  .panel--photo { top: 737px; height: 339px; }
  .panel--photo .panel__photo {
    position: absolute; inset: 0;
    background: radial-gradient(ellipse at 55% 60%, #2c231d 0%, #15110f 70%);
  }

  .logo {
    position: absolute; left: 50%; top: 50%; transform: translate(-50%, -50%);
    display: flex; align-items: center; gap: var(--gap, 12px);
    font-family: "Yanone Kaffeesatz", sans-serif; font-weight: 500;
    font-size: var(--size, 72px); line-height: 0.86;
    color: var(--logo-color, var(--ink));
    white-space: nowrap;
  }
  .logo__dot {
    width: var(--dot, 14px); height: var(--dot, 14px); border-radius: 50%;
    background: var(--logo-color, var(--ink)); align-self: flex-end;
    margin-bottom: calc(var(--size, 72px) * 0.75);
  }
  .logo__name { display: flex; flex-direction: column; }
  .logo__name span:first-child { padding-left: 0.35em; }
  .logo--ink { --logo-color: var(--ink); }
  .logo--brown { --logo-color: var(--brown); }
  .logo--gold { --logo-color: var(--gold); }

  .section-title {
    position: absolute; font-family: "Parisienne", cursive;
    font-size: 30px; color: var(--brown); line-height: 1;
  }

  .label { position: absolute; background: linear-gradient(180deg, #64cbbb 0%, var(--teal) 100%); }
  .label--sheet { left: 635px; top: 90px; width: 493px; height: 274px; }
  .label__rope {
    position: absolute; top: 6px; bottom: 6px; width: 4px;
    border-left: 1px solid #fff; border-right: 1px solid #fff;
  }
  .label__card {
    position: absolute; background: #7fcfc3; padding: 6px;
    box-shadow: 2px 3px 6px rgba(0,0,0,0.25);
  }
  .label__card-inner {
    position: relative; width: 100%; height: 100%;
    background: linear-gradient(180deg, #fff8dc 0%, #fde3c2 100%);
  }
  .label__card-inner::before, .label__card-inner::after {
    content: ""; position: absolute; left: 6px; right: 6px; height: 4px; background: var(--gold);
  }
  .label__card-inner::before { top: 8px; }
  .label__card-inner::after { bottom: 8px; }
  .product-name {
    font-family: "Yanone Kaffeesatz", sans-serif; font-weight: 400;
    color: var(--brown); line-height: 1;
  }
  .product-meta { color: var(--text-body); line-height: 1.45; }
  .label__info { position: absolute; left: 0; right: 0; text-align: center; }

  .swatches { position: absolute; left: 634px; top: 381px; display: flex; gap: 7px; }
  .swatch { width: 34px; height: 32px; }

  .label--flat { left: 626px; top: 640px; width: 171px; height: 144px; }

  .box {
    position: absolute; left: 879px; top: 478px; width: 281px; height: 594px;
    background: var(--paper); box-shadow: 4px 4px 8px rgba(0,0,0,0.25);
  }
  .box__band { position: absolute; left: -2px; right: 0; top: 110px; height: 274px; background: linear-gradient(180deg, #5ec9b8 0%, var(--teal) 100%); }
  .box__info { position: absolute; left: 21px; top: 412px; }
  .box__stripe { position: absolute; left: 5px; right: 6px; bottom: 30px; height: 8px; background: var(--gold); }
</style>
</head>
<body>

  <section class="panel panel--mono">
    <div class="logo logo--ink" style="--size:74px;--dot:14px">
      <span class="logo__dot"></span>
      <span class="logo__name"><span>Nolan</span><span>Whitby</span></span>
    </div>
  </section>

  <section class="panel panel--color">
    <div class="panel__card">
      <div class="logo logo--brown" style="--size:74px;--dot:14px">
        <span class="logo__dot"></span>
        <span class="logo__name"><span>Nolan</span><span>Whitby</span></span>
      </div>
    </div>
  </section>

  <section class="panel panel--photo">
    <div class="panel__photo" role="img" aria-label="Dark still life of an argan oil bottle, a decorated ceramic tagine and argan kernels on a wooden table"></div>
    <div class="logo logo--gold" style="--size:74px;--dot:14px">
      <span class="logo__dot"></span>
      <span class="logo__name"><span>Nolan</span><span>Whitby</span></span>
    </div>
  </section>

  <h2 class="section-title" style="left:646px;top:44px">label</h2>
  <section class="label label--sheet">
    <span class="label__rope" style="left:33px"></span>
    <span class="label__rope" style="left:455px"></span>
    <div class="label__card" style="left:129px;top:8px;width:236px;height:190px">
      <div class="label__card-inner">
        <div class="logo logo--brown" style="--size:56px;--dot:10px;--gap:9px">
          <span class="logo__dot"></span>
          <span class="logo__name"><span>Nolan</span><span>Whitby</span></span>
        </div>
      </div>
    </div>
    <div class="label__info" style="top:210px">
      <p class="product-name" style="font-size:21px">100% pure argan oil</p>
      <p class="product-meta" style="font-size:11px;margin-top:3px">nourishing, moisturizing, revitalizing<br>50ml, 1.7fl oz</p>
    </div>
  </section>

  <div class="swatches">
    <span class="swatch" style="background:var(--teal)"></span>
    <span class="swatch" style="background:var(--teal-light)"></span>
    <span class="swatch" style="background:var(--gold)"></span>
    <span class="swatch" style="background:linear-gradient(90deg,var(--brown-dark),#8a3a10,var(--brown-dark))"></span>
  </div>

  <h2 class="section-title" style="left:610px;top:438px">mock up</h2>
  <section class="label label--flat">
    <div class="label__card" style="left:20px;top:6px;width:131px;height:97px;padding:4px">
      <div class="label__card-inner">
        <div class="logo logo--brown" style="--size:30px;--dot:6px;--gap:5px">
          <span class="logo__dot"></span>
          <span class="logo__name"><span>Nolan</span><span>Whitby</span></span>
        </div>
      </div>
    </div>
    <div class="label__info" style="top:110px">
      <p class="product-name" style="font-size:10px">100% pure argan oil</p>
      <p class="product-meta" style="font-size:6px;margin-top:1px">nourishing, moisturizing, revitalizing<br>50ml, 1.7fl oz</p>
    </div>
  </section>

  <h2 class="section-title" style="left:898px;top:436px">box</h2>
  <section class="box">
    <div class="box__band">
      <div class="label__card" style="left:23px;top:42px;width:240px;height:192px">
        <div class="label__card-inner">
          <div class="logo logo--brown" style="--size:58px;--dot:10px;--gap:9px">
            <span class="logo__dot"></span>
            <span class="logo__name"><span>Nolan</span><span>Whitby</span></span>
          </div>
        </div>
      </div>
    </div>
    <div class="box__info">
      <p class="product-name" style="font-size:20px">100% pure argan oil</p>
      <p class="product-meta" style="font-size:11px;margin-top:3px">nourishing, moisturizing, revitalizing<br>50ml, 1.7fl oz</p>
    </div>
    <span class="box__stripe"></span>
  </section>

</body>
</html>
```